Luxury Caviar Tin Label for High End Caviar Retailer

We are looking for a new caviar label design. We want something unique, preferably black and gold or dark blue and gold. We want a modern and luxurious feel. We have several types of caviar so we need to be able to change the name of the caviar when we print the labels. See inspiration attached. Logo is also attached. More about us: velmoronfare.com

Industry/Entity Type

fine foods industry, caviar

Font styles to use
Serif
Decorative

Requirements
Must have
• KT Velmoron Logo, space for caviar name
Nice to have
• black and gold, blue and gold

```html
<!DOCTYPE html>
<html lang="en">
<head>
<meta charset="utf-8">
<title>KT Velmoron Caviar Tin Label</title>
<link rel="stylesheet" href="https://fonts.googleapis.com/css2?family=Oswald:wght@400;500&family=Marcellus&family=Montserrat:wght@500&display=swap">
<style>
  :root {
    --backdrop: #3a3a3c;
    --navy: #13125e;
    --navy-deep: #0d0c4a;
    --gold: #c9952a;
    --gold-light: #e8cf86;
    --gold-dark: #8a6418;
    --ink-light: #ffffff;
  }
  * { margin: 0; padding: 0; box-sizing: border-box; }
  html, body {
    width: 1200px;
    height: 950px;
    overflow: hidden;
    background: var(--backdrop);
  }
  .label {
    display: block;
    width: 1200px;
    height: 950px;
  }
  .rim { fill: url(#rimGradient); }
  .label-face { fill: url(#faceGradient); }
  .gold-ring { fill: none; stroke: var(--gold); stroke-width: 11; }
  .storage-note {
    font-family: "Oswald", sans-serif;
    font-weight: 500;
    font-size: 38px;
    letter-spacing: 3px;
    fill: var(--ink-light);
  }
  .ingredients-title {
    font-family: "Oswald", sans-serif;
    font-weight: 500;
    font-size: 40px;
    letter-spacing: 1px;
    fill: var(--ink-light);
  }
  .ingredients-list {
    font-family: "Oswald", sans-serif;
    font-weight: 400;
    font-size: 36px;
    letter-spacing: 1px;
    fill: var(--ink-light);
  }
  .brand-name {
    font-family: "Marcellus", serif;
    font-size: 76px;
    letter-spacing: 1px;
    fill: var(--gold);
  }
  .brand-web {
    font-family: "Oswald", sans-serif;
    font-weight: 500;
    font-size: 34px;
    letter-spacing: 4px;
    fill: var(--ink-light);
  }
  .product-name {
    font-family: "Montserrat", sans-serif;
    font-weight: 500;
    font-size: 60px;
    letter-spacing: 9px;
    fill: var(--ink-light);
  }
</style>
</head>
<body>
<svg class="label" viewBox="0 0 1200 950" xmlns="http://www.w3.org/2000/svg">
  <defs>
    <linearGradient id="rimGradient" x1="0" y1="0" x2="1" y2="1">
      <stop offset="0" stop-color="var(--gold-light)"/>
      <stop offset="0.5" stop-color="var(--gold)"/>
      <stop offset="1" stop-color="var(--gold-dark)"/>
    </linearGradient>
    <radialGradient id="faceGradient" cx="0.5" cy="0.5" r="0.55">
      <stop offset="0" stop-color="var(--navy)"/>
      <stop offset="1" stop-color="var(--navy-deep)"/>
    </radialGradient>
    <path id="storageArc" d="M 262 475 A 338 338 0 0 1 938 475"/>
  </defs>

  <circle class="rim" cx="600" cy="475" r="445"/>
  <circle class="label-face" cx="600" cy="475" r="410"/>
  <circle class="gold-ring" cx="600" cy="475" r="388"/>

  <text class="storage-note" text-anchor="middle">
    <textPath href="#storageArc" startOffset="50%">Keep Refrigerated 28-34</textPath>
  </text>

  <text class="ingredients-title" x="600" y="222" text-anchor="middle">Ingredients:</text>
  <text class="ingredients-list" x="600" y="278" text-anchor="middle">Caviar - Salt</text>

  <text class="brand-name" x="600" y="585" text-anchor="middle">KT VELMORON</text>
  <text class="brand-web" x="600" y="640" text-anchor="middle">www.velmoronfare.com</text>

  <text class="product-name" x="600" y="790" text-anchor="middle">CAVIAR</text>
</svg>
</body>
</html>
```